Business card design needed

I need a business card for a new company based in Perth, Western Australia, called KT Power Pty Ltd.

I'm the sole proprietor, and have 25 years' experience in directorship, senior commercial/business development/strategy roles in the oil & gas industry with both supermajors and junior listed companies. I also have interests in renewable energy (and am co-founder and director of a separate renewable energy start-up company). KT Power will be the vehicle for me to contract my services, principally in the oil & gas industry (although this will include directorship services to the renewable energy company). These services will include general consultancy in my areas of expertise, and contracting to provide senior management/director services to start-up or junior oil and gas companies.

I'm looking for a design that communicates professionalism, dynamism, experience, strategic skills and growth.

My Proflinker profile may also be useful context;

"I have a real passion for discovering new investment opportunities and turning them from talk into reality. Right now my focus is on oil, gas and energy ventures. I’m always on the look out for compelling new investment opportunities where I can bring my leadership and strategic insight to bear to make a real difference by delivering transformational results.

I spent 24 years with NX where I built up extensive international experience in oil, gas and energy and was a member of the company’s “fast track” development programme. As an entrepreneurial senior commercial leader, strategic thinker and tactical dealmaker I was responsible for numerous deals such as divestments, farm-ins, asset swaps, new acreage bids, unitizations, gas and LNG sales, creating billions of dollars of value for NX. These deals frequently broke new ground and/or required an innovative approach that delivered results in excess of what the business thought achievable. I have held senior executive and director roles covering Exploration & Production, Mergers & Acquisitions, Business Development, LNG Marketing, Joint Venture Management, Gas & Power and Corporate head office. International assignments included UK, Australia, Indonesia, Norway & Belgium.

I’m a member of the Guild of Global Fuel Brokers (GGFB) and the National Council of Board Officers (NCBO).

Board experience comprises four directorships and two alternate directorships of Australian companies, and directorship of a Not for Profit organisation.

Specialties
Strategy, Business Development, Mergers & Acquisitions, Joint Venture Management, Negotiation, Gas & LNG Marketing."

Target Market(s)

Oil and gas or energy companies of all sizes from large listed companies to start-ups - also service providers to the industry.

Industry/Entity Type

Oil And Gas

Contact Information for Business Card

KT Power Pty Ltd
Martin Dacombe
27C Ferncliff Road,
Holloway Vale,
WA 6999

Tel +61 400 555 817
email dacombemj@quenvol.example.au

```html
<!DOCTYPE html>
<html lang="en">
<head>
<meta charset="utf-8">
<title>KT Power Pty Ltd — Business Card</title>
<link rel="stylesheet" href="https://fonts.googleapis.com/css2?family=Exo+2:wght@400;600;800&display=swap">
<style>
  :root {
    --backdrop: #d9d7d4;
    --card-white: #ffffff;
    --card-black: #151515;
    --brand-red: #c1202d;
    --brand-grey: #5a5a5a;
    --ink: #2e2e2e;
    --text-font: "Exo 2", Arial, sans-serif;
  }
  * { box-sizing: border-box; margin: 0; padding: 0; }
  html, body {
    width: 1200px; height: 600px; overflow: hidden;
    background: var(--backdrop);
    font-family: var(--text-font);
  }
  .stage { position: relative; width: 1200px; height: 600px; }
  .card {
    position: absolute; top: 145px;
    width: 540px; height: 309px;
    box-shadow: 0 6px 18px rgba(0,0,0,0.18);
    overflow: hidden;
  }
  .card--front { left: 40px; background: var(--card-white); }
  .card--back { left: 620px; background: var(--card-black); }

  .brand { position: absolute; display: flex; align-items: center; }
  .brand__square { background: var(--brand-red); flex: none; }
  .brand__name {
    font-weight: 800; color: var(--brand-grey);
    text-transform: uppercase; letter-spacing: 0.02em; line-height: 1;
  }

  .card--front .brand { left: 110px; top: 72px; gap: 12px; }
  .card--front .brand__square { width: 34px; height: 34px; }
  .card--front .brand__name { font-size: 34px; }

  .name-band {
    position: absolute; left: 0; top: 170px;
    width: 255px; height: 26px;
    background: var(--brand-red);
    color: #fff; font-weight: 600; font-size: 16px;
    letter-spacing: 0.04em; text-transform: uppercase;
    display: flex; align-items: center; padding-left: 52px;
  }
  .contact {
    position: absolute; left: 78px; top: 208px;
    color: var(--ink); font-size: 13px; line-height: 1.3;
    text-transform: uppercase; letter-spacing: 0.03em;
  }
  .contact__address { margin-bottom: 10px; }
  .contact__label { color: var(--brand-red); }

  .card--back .brand { left: 60px; top: 92px; gap: 16px; }
  .card--back .brand__square { width: 48px; height: 48px; }
  .card--back .brand__name { font-size: 46px; }

  .services {
    position: absolute; left: 60px; top: 196px; right: 30px;
    color: var(--brand-red); font-size: 11.5px; line-height: 1.45;
    text-transform: uppercase; letter-spacing: 0.04em;
  }
</style>
</head>
<body>
<main class="stage">
  <section class="card card--front" aria-label="Card front">
    <div class="brand">
      <span class="brand__square"></span>
      <span class="brand__name">KT Power Pty Ltd</span>
    </div>
    <div class="name-band">Martin Dacombe</div>
    <div class="contact">
      <p class="contact__address">27C Ferncliff Road, Holloway Vale,<br>WA 6999</p>
      <p><span class="contact__label">P:</span> +61 400 555 817</p>
      <p><span class="contact__label">E:</span> <span style="text-transform:none">dacombemj@quenvol.example.au</span></p>
    </div>
  </section>

  <section class="card card--back" aria-label="Card back">
    <div class="brand">
      <span class="brand__square"></span>
      <span class="brand__name">KT Power Pty Ltd</span>
    </div>
    <p class="services">
      Strategy | Business Development | Mergers &amp; Acquisitions |<br>
      Joint Venture Management | Negotiation | Gas | LNG Marketing
    </p>
  </section>
</main>
</body>
</html>
```